Audio/ Video Packaging Design for a Technology company.

We need a packaging design for a bag that is 7" wide and 10" high. The design will be for a new line of audio/video products. We would like to see designs that represent a superior quality product that provides a pure connection. We want the equivalent of a nice retail bag that you would find in a store like Tallow Mart. It should be a maximum of three colors. We really want something sharp, professional and eye catching, not whimsical or cartoonish. I've included a couple of examples below. I don't really like the designs of the bags, but I want you to see examples of what I'm looking for.

The company logo, which is uploaded, should be on the design. The words "audio and video products" should be either underneath the logo or to the side. Also, somewhere on the bag, we would like the words "For a Pure Connection"

The winner of this contest will likely get the opportunity for additional work as we have more products ready to launch.

Target Market(s)

resellers, consumers - men 25-60

Industry/Entity Type

It Company

Requirements
Must have
• It should be a maximum of three colors. We really want something sharp, professional and eye catching, not whimsical or cartoonish
Nice to have
• Eye-catching design. Utilize the entire bag but don't make it too busy.
Should not have
• Whimsical, cartoonish

```html
<!DOCTYPE html>
<html lang="en">
<head>
<meta charset="utf-8">
<title>Veralink Audio and Video Bag</title>
<link href="https://fonts.googleapis.com/css2?family=Teko:wght@500&family=Josefin+Sans:wght@400&family=Cinzel:wght@400&display=swap" rel="stylesheet">
<style>
  :root {
    --stage: #4a4a4a;
    --foil-light: #f4f4f5;
    --foil-mid: #dcdcde;
    --tab: #2b2b2d;
    --ink: #2c3138;
    --accent: #1aa3e0;
    --green: #3eae8c;
    --teal: #5bbdb3;
    --blue: #3d72b8;
    --navy: #2a57a6;
    --slate: #6f8fb4;
    --lavender: #8e9dcc;
  }
  html, body { margin: 0; padding: 0; overflow: hidden; }
  .canvas {
    width: 1200px; height: 875px; position: relative; overflow: hidden;
    background: var(--stage);
  }
  .bag {
    position: absolute; width: 508px; height: 720px; overflow: hidden;
    border-radius: 26px 26px 4px 4px;
    background: linear-gradient(180deg, var(--foil-light) 0%, #e9e9eb 45%, var(--foil-mid) 100%);
  }
  .bag--front { left: 62px; top: 84px; }
  .bag--back { left: 646px; top: 80px; }
  .bands { position: absolute; inset: 0; width: 508px; height: 720px; }
  .bands line { stroke-linecap: round; opacity: .9; }
  .zipper {
    position: absolute; left: 0; right: 0; top: 90px; height: 30px;
    border-top: 2px solid rgba(0,0,0,.07); border-bottom: 2px solid rgba(0,0,0,.07);
    background: rgba(255,255,255,.35);
  }
  .tab {
    position: absolute; left: 140px; top: 0; width: 228px; height: 78px;
    background: var(--tab); border-radius: 0 0 18px 18px;
    display: flex; align-items: flex-end; justify-content: center; padding-bottom: 8px;
    box-sizing: border-box;
    font-family: 'Teko', sans-serif; font-weight: 500; font-size: 27px; letter-spacing: .5px;
    color: #fff; white-space: nowrap;
  }
  .tab .accent { color: var(--accent); margin-left: 6px; }
  .brand-name {
    font-family: 'Josefin Sans', sans-serif; font-weight: 400; color: var(--ink);
    letter-spacing: 2px; display: flex; align-items: center; gap: 12px; margin: 0;
    white-space: nowrap;
  }
  .brand-name .dot { width: 14px; height: 14px; background: var(--accent); flex: none; }
  .tagline { font-family: 'Cinzel', serif; color: #111; margin: 0; white-space: nowrap; }
  .front-brand { position: absolute; left: 0; right: 0; top: 150px; text-align: center; }
  .front-brand .brand-name { justify-content: center; font-size: 50px; }
  .front-brand .tagline { font-size: 19px; margin-top: 6px; letter-spacing: .5px; }
  .window {
    position: absolute; left: 72px; top: 232px; width: 364px; height: 420px;
    border-radius: 26px;
    background: radial-gradient(ellipse at 40% 20%, #ffffff 0%, #f2f2f3 50%, #dedee0 100%);
    box-shadow: inset 0 0 0 1px rgba(0,0,0,.05);
  }
  .back-brand { position: absolute; left: 120px; width: 270px; top: 330px; text-align: center; }
  .back-brand .brand-name { justify-content: center; font-size: 42px; }
  .back-brand .tagline { font-size: 23px; margin-top: 8px; }
  .back-brand .tagline-large { display: block; font-size: 40px; line-height: 1.05; }
  .media-art {
    position: absolute; left: 0; right: 0; bottom: 0; height: 290px;
    background:
      radial-gradient(ellipse 55% 60% at 50% 95%, rgba(110,110,114,.45) 0%, rgba(150,150,154,.28) 45%, rgba(210,210,212,0) 100%),
      radial-gradient(ellipse 40% 70% at 8% 60%, rgba(140,140,144,.25) 0%, rgba(210,210,212,0) 100%);
  }
</style>
</head>
<body>
<main class="canvas">
  <section class="bag bag--front" aria-label="Bag front">
    <svg class="bands" viewBox="0 0 508 720" aria-hidden="true">
      <line x1="20" y1="300" x2="140" y2="420" stroke="var(--slate)" stroke-width="30"/>
      <line x1="-20" y1="380" x2="120" y2="520" stroke="var(--green)" stroke-width="40"/>
      <line x1="0" y1="460" x2="150" y2="610" stroke="var(--blue)" stroke-width="34"/>
      <line x1="-30" y1="560" x2="130" y2="720" stroke="var(--teal)" stroke-width="36"/>
      <line x1="20" y1="650" x2="120" y2="750" stroke="var(--navy)" stroke-width="30"/>
      <line x1="360" y1="0" x2="508" y2="150" stroke="var(--lavender)" stroke-width="50"/>
      <line x1="420" y1="10" x2="520" y2="110" stroke="var(--teal)" stroke-width="30"/>
      <line x1="380" y1="250" x2="520" y2="390" stroke="var(--blue)" stroke-width="34"/>
      <line x1="420" y1="330" x2="520" y2="430" stroke="var(--green)" stroke-width="40"/>
      <line x1="400" y1="430" x2="520" y2="550" stroke="var(--navy)" stroke-width="36"/>
      <line x1="380" y1="540" x2="520" y2="680" stroke="var(--teal)" stroke-width="40"/>
      <line x1="140" y1="600" x2="260" y2="720" stroke="var(--blue)" stroke-width="30"/>
      <line x1="250" y1="620" x2="360" y2="730" stroke="var(--green)" stroke-width="36"/>
      <line x1="330" y1="600" x2="450" y2="720" stroke="var(--navy)" stroke-width="34"/>
    </svg>
    <div class="zipper"></div>
    <div class="tab">FOR A <span class="accent">PURE CONNECTION</span></div>
    <div class="front-brand">
      <p class="brand-name"><span class="dot"></span>VERALINK</p>
      <p class="tagline">AUDIO AND VIDEO PRODUCTS</p>
    </div>
    <div class="window"></div>
  </section>

  <section class="bag bag--back" aria-label="Bag back">
    <svg class="bands" viewBox="0 0 508 720" aria-hidden="true">
      <line x1="300" y1="100" x2="520" y2="320" stroke="var(--green)" stroke-width="40"/>
      <line x1="350" y1="80" x2="520" y2="250" stroke="var(--slate)" stroke-width="40"/>
      <line x1="430" y1="10" x2="520" y2="100" stroke="var(--teal)" stroke-width="30"/>
      <line x1="400" y1="170" x2="520" y2="290" stroke="var(--lavender)" stroke-width="30"/>
      <line x1="440" y1="420" x2="520" y2="500" stroke="var(--navy)" stroke-width="30"/>
      <line x1="380" y1="520" x2="520" y2="660" stroke="var(--slate)" stroke-width="40"/>
      <line x1="400" y1="600" x2="520" y2="720" stroke="var(--green)" stroke-width="36"/>
    </svg>
    <div class="zipper"></div>
    <div class="tab">FOR A <span class="accent">PURE CONNECTION</span></div>
    <div class="media-art" role="img" aria-label="Illustration of music notes on a staff, film reels and a strip of film"></div>
    <div class="back-brand">
      <p class="brand-name"><span class="dot"></span>VERALINK</p>
      <p class="tagline">AUDIO AND VIDEO <span class="tagline-large">PRODUCTS</span></p>
    </div>
  </section>
</main>
</body>
</html>
```